Marco Delvane 'wait for june' CD cover design

Design a CD cover and a logo (using my initials- MD)
Basically the two files attached are what I'm looking for (front and back)
I'd like my image to stand out with a white background.
The logo will be something I use on all my albums and website.
I like the white bold look.
Possible enhance image marginally I've lost a little weight since taking the picture.
The music I perform is Jazz Swing

Target Market(s)

Jazz Swing Audience

```html
<!DOCTYPE html>
<html lang="en">
<head>
<meta charset="utf-8">
<title>Marco Delvane – wait for june</title>
<link rel="stylesheet" href="https://fonts.googleapis.com/css2?family=Arimo:wght@700&family=Orbitron:wght@500;800&display=swap">
<style>
  :root {
    --sky-white: #fbfbfb;
    --sky-light: #f0f0f0;
    --cloud-grey: rgba(110,110,110,0.38);
    --ground: #ececec;
    --title-light: #e6ec6a;
    --title-dark: #9ea21c;
    --number-light: #7a7a7a;
    --number-dark: #1e1e1e;
    --ink: #0b0b0b;
    --paper: #ffffff;
  }
  html, body {
    margin: 0;
    padding: 0;
    width: 1200px;
    height: 1200px;
    overflow: hidden;
    background: var(--paper);
  }
  .cover {
    position: relative;
    width: 1200px;
    height: 1200px;
    overflow: hidden;
  }
  .sky-backdrop {
    position: absolute;
    inset: 0;
    background:
      radial-gradient(ellipse 34% 16% at 16% 44%, var(--cloud-grey), transparent 70%),
      radial-gradient(ellipse 22% 8% at 10% 22%, rgba(120,120,120,0.22), transparent 70%),
      radial-gradient(ellipse 18% 7% at 90% 18%, rgba(110,110,110,0.3), transparent 70%),
      radial-gradient(ellipse 26% 10% at 30% 8%, rgba(150,150,150,0.18), transparent 70%),
      linear-gradient(180deg, var(--sky-white) 0%, var(--sky-light) 55%, var(--sky-white) 72%, var(--ground) 100%);
  }
  .artist-portrait {
    position: absolute;
    inset: 0;
    width: 1200px;
    height: 1200px;
  }
  .album-title {
    position: absolute;
    left: 32px;
    top: 278px;
    margin: 0;
    font-family: "Orbitron", sans-serif;
    font-weight: 500;
    font-size: 112px;
    line-height: 1;
    letter-spacing: 3px;
    background: linear-gradient(180deg, var(--title-light) 0%, var(--title-dark) 100%);
    -webkit-background-clip: text;
    background-clip: text;
    color: transparent;
  }
  .album-title-accent {
    position: absolute;
    left: 228px;
    top: 398px;
    margin: 0;
    font-family: "Orbitron", sans-serif;
    font-weight: 800;
    font-size: 170px;
    line-height: 1;
    background: linear-gradient(180deg, var(--number-light) 0%, var(--number-dark) 100%);
    -webkit-background-clip: text;
    background-clip: text;
    color: transparent;
  }
  .artist-name {
    position: absolute;
    left: 190px;
    top: 652px;
    margin: 0;
    font-family: "Arimo", sans-serif;
    font-weight: 700;
    font-size: 62px;
    line-height: 1.1;
    color: var(--ink);
  }
  .artist-mark {
    position: absolute;
    right: 52px;
    top: 46px;
    font-family: "Arimo", sans-serif;
    font-weight: 700;
    font-size: 62px;
    line-height: 1;
    color: var(--ink);
  }
  .format-mark {
    position: absolute;
    left: 556px;
    top: 1076px;
    font-family: "Arimo", sans-serif;
    font-weight: 700;
    font-size: 19px;
    letter-spacing: 1px;
    color: var(--paper);
  }
</style>
</head>
<body>
  <main class="cover">
    <div class="sky-backdrop" role="img" aria-label="Black and white cloudy sky over a pale desert landscape"></div>
    <svg class="artist-portrait" viewBox="0 0 1200 1200" role="img" aria-label="Portrait of the artist smiling, wearing a black suit, white shirt and black tie">
      <defs>
        <linearGradient id="portrait-tone" x1="0" y1="0" x2="0" y2="1">
          <stop offset="0" stop-color="#8e8e8e"/>
          <stop offset="0.12" stop-color="#b4b4b4"/>
          <stop offset="0.5" stop-color="#d6d6d6"/>
          <stop offset="0.6" stop-color="#3c3c3c"/>
          <stop offset="1" stop-color="#1e1e1e"/>
        </linearGradient>
      </defs>
      <path fill="url(#portrait-tone)" d="M700,430 C690,260 790,172 915,172 C1050,172 1135,260 1128,430 C1122,560 1090,700 1040,760 L1200,800 L1200,1200 L250,1200 C270,1000 300,880 360,830 C470,760 620,740 740,720 C715,640 700,540 700,430 Z"/>
    </svg>
    <div class="artist-mark">MD</div>
    <h1 class="album-title">wait for</h1>
    <p class="album-title-accent">june</p>
    <h2 class="artist-name">Marco Delvane</h2>
    <div class="format-mark">SoundDisc</div>
  </main>
</body>
</html>
```